Business Card needed for Drainor, a growing Septic Service company

Drainor, a growing local septic service company in Pennsylvania, needs updated business cards. We'd like the business card to feature our logo and communicate that we provide Septic Pumping, Installations/Repairs, Restroom Rentals, and 24/7 Emergency Service. The business card should be eye-catching, bold, and clean/simple. We have been in business almost 10 years and would like to expand and update our business brand and image.

Target Market(s)

Residential and Commercial, New and Current Homeowners

Industry/Entity Type

Service

Contact Information for Business Card

Contact on the business card should be: Dean Harlow Owner & Operator
Phone: 610-555-0187
Email: service@drainor-example.com
Website: www.drainor-example.com
Address: 812 Millbrook Lane Brookvale PA 19990

Font styles to use
Sans Serif

Colors

Designer to choose colors to be used in the design.

Requirements
Must have
• Feature logo on both side of business card.
Nice to have
• We envision the contact information on one side and our services listed on the other side. Utilize the green from the symbol in our logo as part of the design, overall design color scheme should be white, grey, black.

```html
<!DOCTYPE html>
<html lang="en">
<head>
<meta charset="utf-8">
<title>Drainor Business Card</title>
<link rel="stylesheet" href="https://fonts.googleapis.com/css2?family=Arimo:wght@400;700&family=Krona+One&display=swap">
<style>
  :root {
    --bg: #1c1c1c;
    --card: #0c0c0c;
    --card-edge: #1a1a1a;
    --green: #6cbf3a;
    --white: #f2f2f2;
    --grey: #a9a9a9;
    --grey-dark: #8c8c8c;
    --divider: #3a3a3a;
  }
  * { margin: 0; padding: 0; box-sizing: border-box; }
  html, body { width: 1200px; height: 900px; overflow: hidden; }
  body {
    background: var(--bg);
    font-family: "Arimo", Arial, sans-serif;
    display: flex;
    flex-direction: column;
    align-items: center;
    justify-content: center;
    gap: 30px;
  }
  .card {
    width: 700px;
    height: 400px;
    background: var(--card);
    border: 1px solid var(--card-edge);
    border-radius: 26px;
    position: relative;
    overflow: hidden;
  }
  .brand {
    display: flex;
    align-items: center;
    gap: 14px;
  }
  .brand-square {
    width: 46px;
    height: 46px;
    background: var(--green);
    flex: none;
  }
  .brand-name {
    font-family: "Krona One", Arial, sans-serif;
    color: var(--white);
    font-size: 38px;
    letter-spacing: 1px;
    text-transform: uppercase;
    line-height: 1;
  }

  /* contact side */
  .card-front .brand { position: absolute; left: 48px; top: 180px; }
  .card-front .brand-name { font-size: 27px; }
  .card-front .brand-square { width: 36px; height: 36px; }
  .divider {
    position: absolute;
    left: 372px;
    top: 60px;
    bottom: 60px;
    width: 1px;
    background: var(--divider);
  }
  .contact { position: absolute; left: 405px; top: 92px; }
  .contact-name {
    font-family: "Krona One", Arial, sans-serif;
    font-weight: 400;
    color: var(--green);
    font-size: 18px;
    text-transform: uppercase;
    letter-spacing: 0.5px;
  }
  .contact-title { color: var(--grey); font-size: 15px; margin-top: 4px; }
  .contact-list { list-style: none; margin-top: 16px; }
  .contact-list li {
    display: flex;
    align-items: center;
    gap: 9px;
    color: var(--grey);
    font-size: 14.5px;
    line-height: 23px;
  }
  .contact-list svg { width: 14px; height: 14px; flex: none; }
  .address { color: var(--grey-dark); font-size: 15px; line-height: 21px; margin-top: 20px; font-style: normal; }

  /* services side */
  .card-back { display: flex; flex-direction: column; align-items: center; justify-content: center; gap: 50px; }
  .card-back .brand-square { background: var(--white); }
  .services { color: var(--grey); font-size: 15.5px; line-height: 22px; text-align: center; }
  .dot { display: inline-block; width: 6px; height: 6px; border-radius: 50%; background: var(--white); margin: 0 6px 2px; vertical-align: middle; }
</style>
</head>
<body>
  <section class="card card-front" aria-label="Contact side">
    <div class="brand">
      <span class="brand-square"></span>
      <span class="brand-name">Drainor</span>
    </div>
    <div class="divider"></div>
    <div class="contact">
      <h1 class="contact-name">Dean Harlow</h1>
      <p class="contact-title">Owner &amp; Operator</p>
      <ul class="contact-list">
        <li>
          <svg viewBox="0 0 24 24" aria-hidden="true"><path fill="var(--green)" d="M6.6 10.8a15 15 0 0 0 6.6 6.6l2.2-2.2a1 1 0 0 1 1-.25 11.4 11.4 0 0 0 3.6.57 1 1 0 0 1 1 1V20a1 1 0 0 1-1 1A17 17 0 0 1 3 4a1 1 0 0 1 1-1h3.5a1 1 0 0 1 1 1c0 1.25.2 2.45.57 3.570a1 1 0 0 1-.25 1z"/></svg>
          610-555-0187
        </li>
        <li>
          <svg viewBox="0 0 24 24" aria-hidden="true"><rect x="2" y="5" width="20" height="14" fill="var(--green)"/><path d="M2 5l10 8 10-8" fill="none" stroke="#0c0c0c" stroke-width="2"/></svg>
          service@drainor-example.com
        </li>
        <li>
          <svg viewBox="0 0 24 24" aria-hidden="true"><g fill="none" stroke="var(--green)" stroke-width="2"><circle cx="12" cy="12" r="9"/><ellipse cx="12" cy="12" rx="4" ry="9"/><path d="M3 12h18M5 7h14M5 17h14"/></g></svg>
          www.drainor-example.com
        </li>
      </ul>
      <address class="address">812 Millbrook Lane<br>Brookvale PA 19990</address>
    </div>
  </section>

  <section class="card card-back" aria-label="Services side">
    <div class="brand">
      <span class="brand-square"></span>
      <span class="brand-name">Drainor</span>
    </div>
    <p class="services">
      Septic Pumping<span class="dot"></span>Installations/Repairs<br>
      Restroom Rentals<span class="dot"></span>24/7 Emergency Service
    </p>
  </section>
</body>
</html>
```